Office Wall Poster plus other Wall Decal quotes in office

We have redesigned our office & require parts of our Culture statement to be displayed in our office. Our company is VOLO Estate Agents Group and our brand is all about being VOLO .. integrity, honesty, authenticity etc.
We have two areas we wish to decorate.
1. Reception
2. Meeting Room

RECEPTION
We want our leading culture statement to be displayed as large A0 size in a framed POSTER PRINT in our reception. The frame will be black.
WORDING: 'There's a reason we're called VOLO. VOLO is the essence of who we are'
Our brand colors are red, white, black. Our Red is CMYK 12,99, 92,02
When we type our name VOLO, we always use Venera font (always in caps). I have attached a file I personally created with 3 different ideas (I am not a designer) but we are not happy with any of them but it will give you an idea of what we are looking for. We want a simple statement so it stands out and not too busy.

MEETING ROOM
We have one black feature wall in this room and wish to dress this with a collection of quotes from our main Culture statement. We will have these printed as 'stick on wall decals' We have provided a collection of 8 quotes for you to design. Wording is to be in white colour with the key words to be METALLIC SILVER & in caps. We were planning to arrange them ad-hoc on the wall singularly, but if you have any creative ideas on how to display these, we are open to suggestions. Please provide your ideas on how best to arrange these on the black wall. Maybe even in a circle to represent our logo? But we truly do not have a clue - we are only real estate agents, not designers. That is why we would love suggetions on how best to make our Culture Statements work best.
Best of luck and we are excited to see your ideas!

Our clients need to get a great feel for what we are all about when they visit our office. Our culture needs to be seen and felt.

Real Estate

• We use Venera font when we type our name VOLO

EB3D1F
EC4F4E
F09395
F8D3D4
FCEDEE

• Not too busy, simple statements, easy to read

```html
<!DOCTYPE html>
<html lang="en">
<head>
<meta charset="UTF-8">
<title>VOLO Culture Posters</title>
<link rel="stylesheet" href="https://fonts.googleapis.com/css2?family=Kaushan+Script&family=Oswald:wght@700&display=swap">
<style>
  :root {
    --backdrop: #444444;
    --paper: #ffffff;
    --volo-red: #d62029;
    --brand-red: #eb3d1f;
    --wall-black: #000000;
    --chalk: #f4f4f4;
    --silver-light: #f2f2f2;
    --silver-mid: #a8a8a8;
    --silver-dark: #7a7a7a;
    --confetti-tint: #fcedee;
  }
  * { margin: 0; padding: 0; box-sizing: border-box; }
  html, body {
    width: 1200px; height: 1200px; overflow: hidden;
    background: var(--backdrop);
  }
  .canvas { position: relative; width: 1200px; height: 1200px; }

  .poster { position: absolute; overflow: hidden; }
  .poster .line {
    position: absolute; left: 0; right: 0;
    text-align: center; transform: translateY(-50%);
    white-space: nowrap; line-height: 1;
  }

  /* Reception poster */
  .poster--reception {
    left: 84px; top: 266px; width: 500px; height: 704px;
    background: var(--paper);
  }
  .confetti-field {
    position: absolute; inset: 0;
    background: radial-gradient(ellipse at 50% 50%, var(--paper) 35%, var(--confetti-tint) 100%);
  }
  .brand-mark {
    position: absolute; left: 0; right: 0; top: 148px;
    transform: translateY(-50%);
    display: flex; justify-content: center; align-items: center; gap: 8px;
    font-family: "Oswald", sans-serif; font-weight: 700;
    font-size: 30px; color: var(--volo-red); letter-spacing: 1px;
  }
  .brand-mark__dot {
    width: 14px; height: 14px; border-radius: 50%; background: var(--volo-red);
  }
  .statement {
    font-family: "Kaushan Script", cursive; color: var(--volo-red);
  }
  .statement--large { font-size: 66px; }
  .statement--small { font-size: 40px; }
  .statement__name {
    font-family: "Oswald", sans-serif; font-weight: 700;
    font-size: 78px; letter-spacing: 1px; color: var(--volo-red);
  }

  /* Meeting room decal */
  .poster--decal {
    left: 634px; top: 268px; width: 502px; height: 706px;
    background: var(--wall-black);
  }
  .divider {
    position: absolute; left: 0; width: 100%; height: 10px;
    transform: translateY(-50%);
  }
  .quote { font-family: "Kaushan Script", cursive; }
  .quote--plain { color: var(--chalk); font-size: 44px; }
  .quote--key {
    font-size: 52px; text-transform: uppercase; letter-spacing: 1px;
    background: linear-gradient(180deg, var(--silver-light) 0%, var(--silver-mid) 55%, var(--silver-dark) 100%);
    -webkit-background-clip: text; background-clip: text;
    color: transparent;
  }
</style>
</head>
<body>
<main class="canvas">

  <section class="poster poster--reception">
    <div class="confetti-field" role="img" aria-label="Scattered multicolour confetti pieces across a white background"></div>
    <div class="brand-mark"><span class="brand-mark__dot"></span><span>VOLO</span></div>
    <p class="line statement statement--large" style="top:238px">There’s a</p>
    <p class="line statement statement--large" style="top:292px">reason</p>
    <p class="line statement statement--large" style="top:349px">we’re called</p>
    <p class="line statement__name" style="top:427px">VOLO</p>
    <p class="line statement statement--small" style="top:492px">is the essence of</p>
    <p class="line statement statement--small" style="top:530px">who we are</p>
  </section>

  <section class="poster poster--decal">
    <svg class="divider" style="top:92px" viewBox="0 0 502 10" aria-hidden="true">
      <line x1="126" y1="5" x2="230" y2="5" stroke="#ffffff" stroke-width="2"/>
      <circle cx="254" cy="5" r="5" fill="#ffffff"/>
      <line x1="278" y1="5" x2="384" y2="5" stroke="#ffffff" stroke-width="2"/>
    </svg>
    <p class="line quote quote--plain" style="top:162px">Being</p>
    <p class="line quote quote--key" style="top:220px">Genuine</p>
    <p class="line quote quote--plain" style="top:280px">&amp; having</p>
    <p class="line quote quote--key" style="top:350px">True</p>
    <p class="line quote quote--key" style="top:413px">Authenticity</p>
    <p class="line quote quote--plain" style="top:474px; font-size:40px">is paramount to our</p>
    <p class="line quote quote--key" style="top:532px">Good Nature</p>
    <svg class="divider" style="top:592px" viewBox="0 0 502 10" aria-hidden="true">
      <line x1="126" y1="5" x2="230" y2="5" stroke="#ffffff" stroke-width="2"/>
      <circle cx="254" cy="5" r="5" fill="#ffffff"/>
      <line x1="278" y1="5" x2="384" y2="5" stroke="#ffffff" stroke-width="2"/>
    </svg>
  </section>

</main>
</body>
</html>
```